The Winter Orchard Letters

The Winter Orchard Letters ", Author: Maud Ravelier Size: 16 x 24 cm The publisher" Editions Pellor "should be placed on the bottom, with Gill without light Font The books is the portraits of women who had a lover younger or much younger than them

Target Market(s)

General Public

Colors

Designer to choose colors to be used in the design.

Requirements
Must have
• The 11 portraits

```html
<!DOCTYPE html>
<html lang="en">
<head>
<meta charset="utf-8">
<title>The Winter Orchard Letters — Maud Ravelier</title>
<link rel="stylesheet" href="https://fonts.googleapis.com/css2?family=Open+Sans:wght@300;400;600;700&display=swap">
<style>
  :root {
    --page-bg: #dde3e7;
    --cover-core: #5e0204;
    --cover-mid: #3a0103;
    --cover-edge: #160000;
    --ink: #ffffff;
    --frame-edge: #9a9a9a;
    --photo-light: #8d8d8d;
    --photo-dark: #2b2b2b;
  }
  * { box-sizing: border-box; margin: 0; padding: 0; }
  html, body {
    width: 1200px; height: 1200px; overflow: hidden;
    background: var(--page-bg);
    font-family: "Open Sans", sans-serif;
  }
  .book-cover {
    position: absolute;
    left: 256px; top: 84px;
    width: 688px; height: 1032px;
    background: radial-gradient(ellipse 70% 60% at 50% 52%, var(--cover-core) 0%, var(--cover-mid) 55%, var(--cover-edge) 100%);
    color: var(--ink);
    text-align: center;
  }
  .author {
    position: absolute; left: 0; right: 0; top: 52px;
    font-size: 50px; font-weight: 600; letter-spacing: -1.5px;
  }
  .portrait {
    position: absolute;
    border: 2px solid var(--frame-edge);
    background: radial-gradient(ellipse at 50% 40%, var(--photo-light) 0%, #555 45%, var(--photo-dark) 100%);
    box-shadow: inset 0 0 0 3px rgba(0,0,0,0.35);
  }
  .title { position: absolute; left: 0; right: 0; top: 664px; line-height: 1; }
  .title-lead {
    display: block; font-size: 42px; font-weight: 400; letter-spacing: -1px;
  }
  .title-main {
    display: block; font-size: 64px; font-weight: 700; letter-spacing: -2px;
    margin-top: 18px; line-height: 1.18;
  }
  .publisher {
    position: absolute; left: 0; right: 0; top: 938px;
    font-size: 31px; font-weight: 300; letter-spacing: -0.5px;
  }
</style>
</head>
<body>
  <main class="book-cover">
    <h2 class="author">Maud Ravelier</h2>

    <div class="portrait" role="img" aria-label="Black and white portrait of a young woman" style="left:204px;top:200px;width:94px;height:98px"></div>
    <div class="portrait" role="img" aria-label="Black and white portrait of a smiling woman" style="left:309px;top:161px;width:193px;height:136px"></div>
    <div class="portrait" role="img" aria-label="Black and white portrait of an older woman in glasses" style="left:520px;top:230px;width:91px;height:133px"></div>
    <div class="portrait" role="img" aria-label="Black and white portrait of a smiling woman with a necklace" style="left:76px;top:317px;width:132px;height:184px"></div>
    <div class="portrait" role="img" aria-label="Black and white portrait of a nineteenth-century woman" style="left:223px;top:317px;width:132px;height:91px"></div>
    <div class="portrait" role="img" aria-label="Black and white portrait of a woman in a dark dress" style="left:371px;top:317px;width:133px;height:184px"></div>
    <div class="portrait" role="img" aria-label="Black and white portrait of an older smiling woman" style="left:223px;top:427px;width:132px;height:182px"></div>
    <div class="portrait" role="img" aria-label="Black and white portrait of a woman with curly hair" style="left:520px;top:376px;width:91px;height:123px"></div>
    <div class="portrait" role="img" aria-label="Black and white portrait of a laughing woman" style="left:104px;top:518px;width:105px;height:88px"></div>
    <div class="portrait" role="img" aria-label="Black and white portrait of a woman at a podium" style="left:371px;top:518px;width:91px;height:91px"></div>
    <div class="portrait" role="img" aria-label="Black and white portrait of a smiling woman in a collar" style="left:473px;top:518px;width:91px;height:91px"></div>

    <h1 class="title">
      <span class="title-lead">The Winter</span>
      <span class="title-main">Orchard<br>Letters</span>
    </h1>

    <p class="publisher">Editions Pellor</p>
  </main>
</body>
</html>
```